Stationery (Business Cards, Letterheads & Envelopes)

Require stationery design which includes the following items as a minimum.

- Business card design
- Letterhead
- Envelopes

Details for business card:
Logo: Main logo is called "tovell interiors square gold" but you may make use of whichever logo works best.
Tagline: Exquisite Furniture & Furnishings
Name: Mirren Oskaby
Title: Interior Stylist
Mobile: 0427 318 942
PH: 03 9512 3470
Email: mirren@tovell-interiors.com.au

Industry/Entity Type

Business

```html
<!DOCTYPE html>
<html lang="en">
<head>
<meta charset="utf-8">
<title>Tovell Interiors — Stationery</title>
<link href="https://fonts.googleapis.com/css2?family=Cinzel:wght@400&family=Montserrat:wght@300;400&display=swap" rel="stylesheet">
<style>
  :root{
    --bg:#dedede;
    --paper:#f8f8f8;
    --ink:#1b1b1b;
    --grey:#8a8a8a;
    --gold:#c7a94e;
    --faint:#ececec;
  }
  *{box-sizing:border-box;margin:0;padding:0}
  html,body{width:769px;height:1200px;overflow:hidden;background:var(--bg)}
  body{font-family:'Montserrat',sans-serif;color:var(--ink)}
  .set{position:relative;width:769px;height:400px;background:linear-gradient(#e8e8e8,var(--bg))}
  .set + .set{border-top:1px solid #d2d2d2}

  .brand{font-family:'Cinzel',serif;font-weight:400;letter-spacing:.16em;display:flex;align-items:center;gap:5px;line-height:1;white-space:nowrap}
  .brand .dot{width:.55em;height:.55em;border-radius:50%;background:currentColor;flex:none}
  .brand .words{display:flex;flex-direction:column;align-items:center;gap:2px}
  .brand .sub{font-size:.42em;letter-spacing:.3em}

  .scene-logo{position:absolute;left:36px;top:30px;font-size:22px;color:#7f7f7f}

  .card{position:absolute;left:174px;width:74px;height:38px;box-shadow:0 1px 3px rgba(0,0,0,.2)}
  .card-front{top:120px;background:var(--ink);display:flex;align-items:center;justify-content:center}
  .card-front .brand{font-size:6px;color:var(--gold)}
  .card-back{top:166px;background:var(--paper);padding:5px 6px}
  .card-back .brand{font-size:4px;color:var(--ink);margin-bottom:4px}
  .card-back .name{font-size:3.4px;letter-spacing:.08em;text-transform:uppercase}
  .card-back .title{font-size:3px;color:var(--gold);margin-bottom:2px}
  .card-back .contact{font-size:2.6px;line-height:1.4;color:#555;font-weight:300}

  .letterhead{position:absolute;left:290px;top:46px;width:159px;height:279px;background:var(--paper);box-shadow:0 1px 4px rgba(0,0,0,.15);padding:14px 15px}
  .letterhead .brand{font-size:7px;color:var(--ink);margin-bottom:14px}
  .letterhead .brand .dot{color:var(--gold)}
  .letter{position:relative;z-index:1;font-size:3.4px;line-height:1.6;color:#555;font-weight:300}
  .letter p{margin-bottom:4px}
  .letter .sign{margin-top:8px;font-weight:400;color:var(--ink)}
  .letterhead .pattern{position:absolute;left:52px;top:70px;width:90px;height:90px;border-radius:50%;background:radial-gradient(#eeeeee,var(--paper) 70%)}
  .letterhead .foot{position:absolute;left:0;right:0;bottom:0;height:4px;background:var(--ink)}
  .letterhead .foot::after{content:"";position:absolute;right:0;top:0;width:28px;height:100%;background:var(--gold)}

  .envelope{position:absolute;left:495px;width:185px;background:var(--paper);box-shadow:0 1px 4px rgba(0,0,0,.15);overflow:hidden}
  .env-front{top:77px;height:90px;padding:0}
  .env-front .brand{position:absolute;left:50%;top:16px;transform:translateX(-50%);font-size:6px;color:var(--ink)}
  .env-front .brand .dot{color:var(--gold)}
  .env-front .pattern{position:absolute;right:-14px;top:8px;width:70px;height:70px;border-radius:50%;background:radial-gradient(#ece3c6,var(--paper) 70%)}
  .v2 .env-front .pattern,.v3 .env-front .pattern{background:radial-gradient(#e6e6e6,var(--paper) 70%)}
  .env-back{top:174px;height:87px}
  .env-back .flap{position:absolute;left:0;top:0;width:100%;height:28px;background:var(--ink)}
  .env-back .band{position:absolute;left:32px;right:32px;top:22px;height:2px;background:var(--gold)}
  .v1 .env-back .band{display:none}
  .v3 .env-back .flap{background:var(--faint)}
  .v3 .env-back .band{left:80px;right:80px;top:48px;height:1px;background:#cfcfcf}
</style>
</head>
<body>

<section class="set v1">
  <div class="brand scene-logo"><span class="words">Tovell<span class="sub">Interiors</span></span></div>
  <div class="card card-front"><div class="brand"><span class="dot"></span><span class="words">Tovell<span class="sub">Interiors</span></span></div></div>
  <div class="card card-back">
    <div class="brand"><span class="words">Tovell<span class="sub">Interiors</span></span></div>
    <div class="name">Mirren Oskaby</div>
    <div class="title">Interior Stylist</div>
    <div class="contact">M 0427 318 942<br>P 03 9512 3470<br>mirren@tovell-interiors.com.au</div>
  </div>
  <article class="letterhead">
    <div class="pattern" role="img" aria-label="Faint decorative pattern"></div>
    <div class="brand"><span class="dot"></span><span class="words">Tovell<span class="sub">Interiors</span></span></div>
    <div class="letter">
      <p>Ms Jane Hallow<br>12 Elm Road, Kew</p>
      <p>Dear Jane,</p>
      <p>Thank you for choosing us to style your new home.<br>Our team will contact you shortly.</p>
      <p>Kind regards,</p>
      <p class="sign">Mirren Oskaby</p>
    </div>
    <div class="foot"></div>
  </article>
  <div class="envelope env-front">
    <div class="pattern" role="img" aria-label="Gold decorative pattern"></div>
    <div class="brand"><span class="dot"></span><span class="words">Tovell<span class="sub">Interiors</span></span></div>
  </div>
  <div class="envelope env-back"><div class="flap"></div><div class="band"></div></div>
</section>

<section class="set v2">
  <div class="brand scene-logo"><span class="words">Tovell<span class="sub">Interiors</span></span></div>
  <div class="card card-front"><div class="brand"><span class="dot"></span><span class="words">Tovell<span class="sub">Interiors</span></span></div></div>
  <div class="card card-back">
    <div class="brand"><span class="words">Tovell<span class="sub">Interiors</span></span></div>
    <div class="name">Mirren Oskaby</div>
    <div class="title">Interior Stylist</div>
    <div class="contact">M 0427 318 942<br>P 03 9512 3470<br>mirren@tovell-interiors.com.au</div>
  </div>
  <article class="letterhead">
    <div class="pattern" role="img" aria-label="Faint decorative pattern"></div>
    <div class="brand"><span class="dot"></span><span class="words">Tovell<span class="sub">Interiors</span></span></div>
    <div class="letter">
      <p>Ms Jane Hallow<br>12 Elm Road, Kew</p>
      <p>Dear Jane,</p>
      <p>Thank you for choosing us to style your new home.<br>Our team will contact you shortly.</p>
      <p>Kind regards,</p>
      <p class="sign">Mirren Oskaby</p>
    </div>
    <div class="foot"></div>
  </article>
  <div class="envelope env-front">
    <div class="pattern" role="img" aria-label="Grey decorative pattern"></div>
    <div class="brand"><span class="dot"></span><span class="words">Tovell<span class="sub">Interiors</span></span></div>
  </div>
  <div class="envelope env-back"><div class="flap"></div><div class="band"></div></div>
</section>

<section class="set v3">
  <div class="brand scene-logo"><span class="words">Tovell<span class="sub">Interiors</span></span></div>
  <div class="card card-front"><div class="brand"><span class="dot"></span><span class="words">Tovell<span class="sub">Interiors</span></span></div></div>
  <div class="card card-back">
    <div class="brand"><span class="words">Tovell<span class="sub">Interiors</span></span></div>
    <div class="name">Mirren Oskaby</div>
    <div class="title">Interior Stylist</div>
    <div class="contact">M 0427 318 942<br>P 03 9512 3470<br>mirren@tovell-interiors.com.au</div>
  </div>
  <article class="letterhead">
    <div class="pattern" role="img" aria-label="Faint decorative pattern"></div>
    <div class="brand"><span class="dot"></span><span class="words">Tovell<span class="sub">Interiors</span></span></div>
    <div class="letter">
      <p>Ms Jane Hallow<br>12 Elm Road, Kew</p>
      <p>Dear Jane,</p>
      <p>Thank you for choosing us to style your new home.<br>Our team will contact you shortly.</p>
      <p>Kind regards,</p>
      <p class="sign">Mirren Oskaby</p>
    </div>
    <div class="foot"></div>
  </article>
  <div class="envelope env-front">
    <div class="pattern" role="img" aria-label="Grey decorative pattern"></div>
    <div class="brand"><span class="dot"></span><span class="words">Tovell<span class="sub">Interiors</span></span></div>
  </div>
  <div class="envelope env-back"><div class="flap"></div><div class="band"></div></div>
</section>

</body>
</html>
```